The maple crew

I want it as prefession and attractive as possible we are a lawnmowing business

Phone number 605-318-2264
Name- Carlos Whitfield
Email- themaplecrewsd@fernpost.com

```html
<!DOCTYPE html>
<html lang="en">
<head>
<meta charset="UTF-8">
<title>The Maple Crew — Business Card</title>
<link href="https://fonts.googleapis.com/css2?family=Montserrat:wght@700&family=Quicksand:wght@500&display=swap" rel="stylesheet">
<style>
  :root {
    --bg: #3b3b3b;
    --green-light: #5cb342;
    --green-mid: #3a8f2c;
    --green-dark: #1e661c;
    --green-brand: #2f7d2a;
    --green-name: #4aab35;
    --paper: #ffffff;
    --paper-shade: #e9e9e9;
    --ink: #333333;
    --rule: #555555;
  }
  * { box-sizing: border-box; margin: 0; padding: 0; }
  html, body {
    width: 1200px; height: 900px; overflow: hidden;
    background: var(--bg);
  }
  .canvas {
    width: 1200px; height: 900px;
    display: flex; flex-direction: column;
    align-items: center; justify-content: center; gap: 40px;
  }
  .card {
    width: 700px; height: 400px;
    border-radius: 34px;
    position: relative;
    overflow: hidden;
  }
  .card--front {
    background: radial-gradient(ellipse at 50% 55%, var(--green-light) 0%, var(--green-mid) 50%, var(--green-dark) 100%);
    display: flex; align-items: center; justify-content: center;
  }
  .brand {
    display: flex; align-items: center; gap: 16px;
    font-family: "Montserrat", sans-serif;
    font-weight: 700;
    text-transform: uppercase;
    letter-spacing: 1px;
  }
  .brand__mark { width: 22px; height: 22px; }
  .card--front .brand { color: var(--paper); font-size: 46px; }
  .card--front .brand__mark { background: var(--paper); }
  .card--back {
    background: linear-gradient(120deg, var(--paper) 0%, var(--paper-shade) 55%, var(--paper) 100%);
  }
  .card--back .brand {
    position: absolute; left: 48px; top: 56px;
    color: var(--green-brand); font-size: 34px;
  }
  .card--back .brand__mark { width: 18px; height: 18px; background: var(--green-brand); }
  .contact-block {
    position: absolute; right: 44px; bottom: 70px;
    display: flex; align-items: center; gap: 22px;
  }
  .person-name {
    font-family: "Montserrat", sans-serif; font-weight: 700;
    font-size: 26px; color: var(--green-name);
    text-transform: uppercase; letter-spacing: 1px;
  }
  .divider { width: 1.5px; height: 64px; background: var(--rule); }
  .contact-list { list-style: none; display: flex; flex-direction: column; gap: 10px; }
  .contact-list li {
    display: flex; align-items: center; gap: 10px;
    font-family: "Quicksand", sans-serif; font-weight: 500;
    font-size: 19px; color: var(--ink);
  }
  .contact-list svg { width: 18px; height: 18px; fill: var(--green-name); flex: none; }
</style>
</head>
<body>
<main class="canvas">
  <section class="card card--front" aria-label="Card front">
    <div class="brand"><span class="brand__mark"></span><span>The maple crew</span></div>
  </section>

  <section class="card card--back" aria-label="Card back">
    <div class="brand"><span class="brand__mark"></span><span>The maple crew</span></div>
    <div class="contact-block">
      <p class="person-name">Carlos Whitfield</p>
      <span class="divider"></span>
      <ul class="contact-list">
        <li>
          <svg viewBox="0 0 24 24" aria-hidden="true"><path d="M6.6 10.8a15 15 0 0 0 6.6 6.6l2.2-2.2c.3-.3.7-.4 1-.2 1.1.4 2.3.6 3.6.6.6 0 1 .4 1 1V20c0 .6-.4 1-1 1A17 17 0 0 1 3 4c0-.6.4-1 1-1h3.5c.6 0 1 .4 1 1 0 1.3.2 2.5.6 3.6.1.3 0 .7-.2 1z"/></svg>
          <span>605-318-2264</span>
        </li>
        <li>
          <svg viewBox="0 0 24 24" aria-hidden="true"><path d="M2 5h20v14H2zm2 2v.5l8 5 8-5V7zm0 2.8V17h16V9.8l-8 5z"/></svg>
          <span>themaplecrewsd@fernpost.com</span>
        </li>
      </ul>
    </div>
  </section>
</main>
</body>
</html>
```